Stock Broking Firm - Web Design Project

We are looking at doing a full re-design of our home page and content page and moving the majority of our content over to DNN.

Phase 1 : Website redesign www.kalvernequities.com.au

The current design is too washed out, boring and has no call to action buttons.

Solution:

KL Equities is looking for a brighter/ cleaner redesign with a few stand out call to action buttons.

• Banner with logo across the top horizontally - Bright blue logo on white background similar to www.dmq.com.au - CALL 1300 482 917 - Follow on Chirper / Facespace
• Horizontal menu bar - professional looking. - Home - About Us- Our Services - Membership - Open an Account - Become a member - Contact
• Below banner top left - large rotating banner - maybe zimbo gallery style www.tvhaldrens.com.au
• Right of rotating banner - Membership login
• Below members login - Register for Daily Market Report/ research blog - Large bright button / Name / Email / Phone / pop up??
• Below Register for daily market report - Market Indicies - RSS feed of delayed data from QNW see www.tvhaldrens.com
• Below Market indicies - KL EQUITIES - Market Tweets ( feed from our chirper page)

Below Rotating Banner -

content area

Below content area - 4 large block buttons see www.crandwickley.com.au ( hover over change colour)

Button 1 - EDUCATION - content - click here for more

Button 2 - Market Information and Research

Button 3 - Full service Broker - content brief - click here for more

Button 4 - Trade Commodities and Options

below buttons - small horizontal menu bar slightly different colour incl - Careers/ Partners / Legal Privacy FSG Site Map

Regards,
Colin Marsh

Target Market(s)

35 - 65

Industry/Entity Type

Education

Requirements
Must have
• Follow brief above - large banner, call to action buttons, F.S. Chirper, Member login etc. 4 big buttons
Nice to have
• clean looking site similar to www.dmq.com.au / not too busy. Corporate looking.
Should not have
• not too busy

```html
<!DOCTYPE html>
<html lang="en">
<head>
<meta charset="utf-8">
<title>KL Equities</title>
<link href="https://fonts.googleapis.com/css2?family=Open+Sans:wght@400;600;700&display=swap" rel="stylesheet">
<style>
:root{
  --blue:#1597d5;
  --blue-dark:#0a7fc0;
  --blue-text:#0b86c8;
  --navy:#2f3f50;
  --slate:#3d5a70;
  --text:#555;
  --muted:#8a8a8a;
  --line:#e2e2e2;
  --row:#e4f3fa;
  --red:#d01818;
  --green:#2f9a2f;
  --gold:#f4c20f;
}
*{box-sizing:border-box;margin:0;padding:0}
html,body{width:805px;height:1200px;overflow:hidden;background:#fff}
body{font-family:"Open Sans",Arial,sans-serif;color:var(--text);position:relative}
.page{position:absolute;left:98px;top:0;width:610px;height:1200px;background:#fff;box-shadow:0 0 6px rgba(0,0,0,.18)}
.abs{position:absolute}
a{color:var(--blue-text);text-decoration:none}

/* header */
.brand{left:107px;top:16px}
.brand-name{font-size:34px;font-weight:400;color:#1a6f9c;line-height:38px;letter-spacing:-.3px}
.brand-tag{font-size:7.5px;color:#444;text-align:right;width:230px;line-height:10px;margin-top:2px}
.call{left:567px;top:12px;width:131px;height:37px;background:var(--slate);color:#fff;padding:4px 0 0 28px}
.call svg{position:absolute;left:9px;top:9px}
.call small{display:block;font-size:11px;line-height:12px}
.call strong{display:block;font-size:15px;font-weight:600;line-height:17px}
.follow{right:107px;top:64px;font-size:11px;color:#555;display:flex;align-items:center;gap:6px}
.follow .soc{font-size:10px;font-weight:600;color:var(--blue-text)}

/* nav */
.nav{left:107px;top:94px;width:591px;height:24px;background:linear-gradient(#2cb3e8,#0b8bcc);display:flex;justify-content:space-around;align-items:center}
.nav a{color:#fff;font-size:11px;font-weight:600}

/* slider */
.slider{left:107px;top:131px;width:412px;height:239px;border:1px solid #d8d8d8}
.slide-img{position:absolute;left:2px;top:2px;width:406px;height:135px;background:linear-gradient(100deg,#eef5fb,#c9dcec 55%,#e9f1f8)}
.slide-title{position:absolute;left:6px;top:142px;font-size:10.5px;font-weight:600;color:var(--blue-text)}
.slide-sub{position:absolute;left:6px;top:156px;font-size:8.5px;color:#333}
.thumbs{position:absolute;left:0;top:175px;width:410px;height:45px;border-top:1px solid #ddd;border-bottom:1px solid #ddd;display:flex;gap:7px;padding:4px 5px}
.thumb{width:51px;height:35px;background:linear-gradient(#dfe8ef,#b8cad8)}
.thumb.green{background:linear-gradient(#9cc7e6,#4e8a3c)}
.thumb.active{background:#3e5060;outline:3px solid #3e5060}
.pager{position:absolute;left:7px;top:224px;font-size:7.5px;color:#777}
.pager-ctl{position:absolute;right:4px;top:222px;display:flex}
.pager-ctl span{width:15px;height:11px;border:1px solid #aaa;font-size:7px;line-height:9px;text-align:center;color:#333}

/* content */
.content{left:107px;top:385px;width:412px;font-size:8.3px;line-height:11.4px}
.content h1{font-size:11px;font-weight:600;color:var(--blue-text);padding-bottom:6px;border-bottom:1px solid var(--line);margin-bottom:12px}
.content p{margin-bottom:12px}
.adv{list-style:none;margin:0 0 12px 10px}
.adv li{position:relative;padding-left:21px;margin-bottom:10px}
.adv .num{position:absolute;left:0;top:0;width:13px;height:13px;border-radius:50%;background:#e6e6e6;font-size:7.5px;line-height:13px;text-align:center;color:#333}
.services a{margin:0 5px}

/* feature blocks */
.feature{width:199px;height:104px;border:1px solid #dadada;border-radius:2px;background:linear-gradient(#fff,#ececec);padding:10px 11px;font-size:8.3px;line-height:11.4px;color:#444}
.feature h2{font-size:10.5px;font-weight:700;color:var(--blue-text);line-height:12px;height:27px;text-transform:uppercase}
.feature.two h2{height:27px}
.feature.active{background:linear-gradient(#25a9e6,#1188cc);border-color:#1188cc;color:#fff}
.feature.active h2,.feature.active a{color:#fff}
.feature a{display:block;margin-top:3px}

/* sidebar */
.panel-head{height:28px;background:var(--navy);color:#fff;font-size:10.5px;font-weight:600;padding:8px 0 0 12px;border-bottom:2px solid #1ea3df;position:relative}
.panel-head svg{position:absolute;right:12px;top:7px}
.login{left:532px;top:133px;width:166px;height:175px}
.login-body{background:#159ad8;height:147px;padding:10px 11px;color:#fff;font-size:9.5px}
.login-body input{display:block;width:100%;height:20px;border:none;border-radius:3px;margin:4px 0 10px}
.login-links{font-size:7.5px;margin-top:-4px}
.login-btn{display:block;width:142px;height:20px;margin:9px 0 0;border-radius:4px;background:linear-gradient(#fde268,var(--gold));color:#333;font-size:12px;font-weight:600;text-align:center;line-height:20px}
.register{left:532px;top:321px;width:166px;height:49px;background:linear-gradient(#32b1ea,#0c8acb);color:#fff;font-size:12.5px;font-weight:600;text-align:center;line-height:16px;padding-top:8px}
.indices{left:532px;top:384px;width:166px;border:1px solid #ddd;border-top:none}
.indices table{width:100%;border-collapse:collapse;font-size:7.5px}
.indices th{color:var(--blue-text);font-size:8.5px;font-weight:600;height:20px}
.indices td{height:15.3px;padding:0 3px;color:#333}
.indices tr:nth-child(even) td{background:var(--row)}
.neg{color:var(--red)}.pos{color:var(--green)}
.news{left:532px;top:563px;width:166px;height:258px;border:1px solid #ddd;border-top:none}
.news ul{list-style:none;padding:4px 8px 0}
.news li{display:flex;gap:6px;font-size:7.8px;line-height:11px;padding:4px 0 3px;border-bottom:1px solid #eee;height:30px}
.news time{color:#444;white-space:nowrap}
.news-foot{position:absolute;left:12px;bottom:4px;right:8px;display:flex;justify-content:space-between;align-items:center;font-size:8px}
.news-foot b{color:#1b4e7c}
.news-foot span{border:1px solid #ccc;border-radius:2px;padding:0 6px;background:#f4f4f4;color:#333}
.tweets{left:532px;top:838px;width:166px;height:234px;border:1px solid #ddd;border-top:none}
.tweets .panel-head{height:33px;padding-top:4px;line-height:11px}
.tweets ul{list-style:none;padding:12px 10px 0}
.tweets li{font-size:7.8px;line-height:11px;color:#333;padding-bottom:8px;margin-bottom:10px;border-bottom:1px solid #eee}
.tweets small{display:block;color:var(--muted);font-size:7px;margin-top:3px}
.tweets .follow-link{font-size:8px;padding-left:10px;display:flex;gap:4px;align-items:center}

/* footer */
.footer{left:107px;top:1158px;width:591px;border-top:1px solid var(--line);padding-top:5px;font-size:8px}
.footer-links a{margin-right:2px}
.footer-copy{color:#333;margin-top:2px}
.footer-right{position:absolute;right:0;top:12px;display:flex;gap:12px;align-items:center;color:#333}
</style>
</head>
<body>
<div class="page"></div>

<header>
  <div class="abs brand">
    <div class="brand-name">KL Equities</div>
    <div class="brand-tag">shares | options | commodities | foreign exchange<br>ABN 72 305 846 119 | licence no 528 406</div>
  </div>
  <div class="abs call">
    <svg width="12" height="18" viewBox="0 0 12 18"><rect x="1" y="1" width="10" height="16" rx="1.5" fill="#f4c20f"/><rect x="3" y="3" width="6" height="6" fill="#3d5a70"/></svg>
    <small>Call</small><strong>1300 482 917</strong>
  </div>
  <div class="abs follow">Follow on <span class="soc">Facespace</span><span class="soc">Chirper</span></div>
  <nav class="abs nav">
    <a href="#">Home</a><a href="#">About Us</a><a href="#">Our Services</a><a href="#">Membership</a><a href="#">Open an Account</a><a href="#">Become a member</a><a href="#">Contact</a>
  </nav>
</header>

<section class="abs slider">
  <div class="slide-img" role="img" aria-label="Rotating banner photo: hand drawing a rising red market chart line"></div>
  <div class="slide-title">Lorem ipsum dolor sit amet,</div>
  <div class="slide-sub">Lorem ipsum dolor sit amet, consectetur adipisicing elit, sed do eiusmod</div>
  <div class="thumbs">
    <div class="thumb green" role="img" aria-label="Thumbnail: field"></div>
    <div class="thumb" role="img" aria-label="Thumbnail: paperwork"></div>
    <div class="thumb" role="img" aria-label="Thumbnail: business meeting"></div>
    <div class="thumb" role="img" aria-label="Thumbnail: charts"></div>
    <div class="thumb active" role="img" aria-label="Thumbnail: rising chart"></div>
    <div class="thumb" role="img" aria-label="Thumbnail: graph"></div>
    <div class="thumb" role="img" aria-label="Thumbnail: globe"></div>
  </div>
  <div class="pager">37 - 40 OF 44</div>
  <div class="pager-ctl"><span>&lsaquo;</span><span>II</span><span>&rsaquo;</span></div>
</section>

<main class="abs content">
  <h1>Welcome to KL Equities</h1>
  <p>KL Equities is a full-service brokerage company located on the Gold Coast (Australia). Our company trades Australian stocks, options on Australian stocks, commodities (gold, silver, light oil) and CFD through Harrowgate trading platform on behalf of our clients.</p>
  <p>Our main advantages are :</p>
  <ol class="adv">
    <li><span class="num">1</span><a href="#">Higher potential return</a>. Trading options on Australian stocks or commodities such as gold and silver, you spend much less money and make almost the same profit as if you buy or sell Australian stocks.</li>
    <li><span class="num">2</span><a href="#">Low Brokerage</a> commission and cost efficiency. Options have great leveraging power. You can obtain an option position that will mimic your stock position almost identically, but at a huge cost savings.</li>
    <li><span class="num">3</span><a href="#">Comprehensive education</a>.  Many investors have avoided options and commodities, believing them to be sophisticated and, therefore, too difficult to understand. Many more have had bad initial experiences with options because neither they nor their brokers were properly trained in how to use them. The improper use of options, like that of any powerful tool, can lead to major problems. If you become a KL Equities Member, we will teach you how to trade options for FREE!!! Furthermore, you will get access to our research and daily reports.</li>
  </ol>
  <p>Our main objective is to increase clients' wealth by regularly reviewing their trading portfolio, providing research and education and simplifying their trading through a personalised and professional service.</p>
  <p>We believe that constant communication with our clients' allows for transparency in what we do and ensures a long term relationship built on trust and commitment.</p>
  <p>Whether you are an experienced trader or have just started your portfolio, KL Equities welcomes you with a commitment to profitable trading and superior client/advisor relationships.</p>
  <p>Our unique blend of experience across funds management and technical analysis coupled with enthusiasm and drive for success, creates the perfect climate for you to capitalise on your resources.</p>
  <p>KL Equities offers a full range of products and services from which you can choose:</p>
  <p class="services"><a href="#" style="margin-left:0">KL MEMBERSHIP</a> | <a href="#">BROKERAGE</a> | <a href="#">EDUCATION &amp; MENTORING</a> | <a href="#">RESEARCH</a></p>
  <p>For more information on how you can benefit from being a KL Equities Member, call one of our friendly consultants today on <b>+61 (0) 7 5581 2260</b>. sign up for a free <a href="#">7 DAY TRIAL</a> or contact us via our contact page for a FREE one on one consultation.</p>
  <p>&nbsp;KL Equities (QLD) Pty Ltd holds an Australian Financial Services License (AFSL: 528406)</p>
</main>

<section>
  <div class="abs feature active" style="left:107px;top:909px">
    <h2>Education</h2>
    Lorem ipsum dolor sit amet, consectetur adipisicing elit, sed do eiusmod tempor incididunt ut labore et dolore magna aliqua. Ut enim ad minim veniam...
    <a href="#">Click here for more +</a>
  </div>
  <div class="abs feature two" style="left:320px;top:909px">
    <h2>Market Information<br>and Research</h2>
    Lorem ipsum dolor sit amet, consectetur adipisicing elit, sed do eiusmod tempor incididunt ut labore et dolore magna aliqua. Ut enim ad minim veniam...
    <a href="#">Click here for more +</a>
  </div>
  <div class="abs feature" style="left:107px;top:1027px">
    <h2>Full Service Broker</h2>
    Lorem ipsum dolor sit amet, consectetur adipisicing elit, sed do eiusmod tempor incididunt ut labore et dolore magna aliqua. Ut enim ad minim veniam...
    <a href="#">Click here for more +</a>
  </div>
  <div class="abs feature two" style="left:320px;top:1027px">
    <h2>Trade Commodities<br>and Options</h2>
    Lorem ipsum dolor sit amet, consectetur adipisicing elit, sed do eiusmod tempor incididunt ut labore et dolore magna aliqua. Ut enim ad minim veniam...
    <a href="#">Click here for more +</a>
  </div>
</section>

<aside>
  <div class="abs login">
    <div class="panel-head">MEMBERSHIP LOGIN
      <svg width="14" height="14" viewBox="0 0 14 14"><circle cx="7" cy="4" r="3" fill="#f0a040"/><rect x="2" y="8" width="10" height="6" rx="2" fill="#e0522a"/></svg>
    </div>
    <div class="login-body">
      <label>Username<input type="text" aria-label="Username"></label>
      <label>Password<input type="password" aria-label="Password"></label>
      <div class="login-links">Register &nbsp;|&nbsp; Forgot Password</div>
      <span class="login-btn">LOGIN</span>
    </div>
  </div>

  <a class="abs register" href="#">Register for Daily Market<br>Report / research blog</a>

  <div class="abs indices">
    <div class="panel-head">MARKET INDICIES
      <svg width="20" height="12" viewBox="0 0 20 12"><polyline points="1,4 6,10 10,4 14,10 19,2" fill="none" stroke="#3cc04a" stroke-width="2.5"/></svg>
    </div>
    <table>
      <tr><th>Name</th><th>Value</th><th>+/-</th><th>%+/-</th></tr>
      <tr><td>AllShr</td><td>4,511.90</td><td class="neg">-14.70</td><td class="neg">-0.32</td></tr>
      <tr><td>KX200</td><td>4,490.74</td><td class="neg">-14.56</td><td class="neg">-0.32</td></tr>
      <tr><td>Dral</td><td>13,434.05</td><td class="neg">-39.48</td><td class="neg">-0.29</td></tr>
      <tr><td>HKIdx</td><td>20,919.60</td><td class="neg">-17.68</td><td class="neg">-0.08</td></tr>
      <tr><td>TECHX</td><td>3,066.87</td><td class="pos">+1.85</td><td class="pos">+0.06</td></tr>
      <tr><td>JP225</td><td>8,596.23</td><td class="neg">-173.36</td><td class="neg">-1.98</td></tr>
      <tr><td>US500</td><td>1,441.48</td><td>-</td><td>-</td></tr>
    </table>
  </div>

  <div class="abs news">
    <div class="panel-head">BREAKING NEWS
      <svg width="12" height="12" viewBox="0 0 12 12"><rect width="12" height="12" rx="2" fill="#f08a1c"/><circle cx="3" cy="9" r="1.3" fill="#fff"/><path d="M2 5a5 5 0 0 1 5 5M2 2a8 8 0 0 1 8 8" stroke="#fff" stroke-width="1.4" fill="none"/></svg>
    </div>
    <ul>
      <li><time>11:43 PM</time><a href="#">Norvale says India could see rating cut</a></li>
      <li><time>11:43 PM</time><a href="#">Norvale says India could see rating cut</a></li>
      <li><time>11:43 PM</time><a href="#">Norvale says India could see rating cut</a></li>
      <li><time>11:43 PM</time><a href="#">Norvale says India could see rating cut</a></li>
      <li><time>11:43 PM</time><a href="#">Norvale says India could see rating cut</a></li>
      <li><time>11:43 PM</time><a href="#">Norvale says India could see rating cut</a></li>
      <li><time>11:43 PM</time><a href="#">Norvale says India could see rating cut</a></li>
    </ul>
    <div class="news-foot"><b>QNW</b><span>Read more +</span></div>
  </div>

  <div class="abs tweets">
    <div class="panel-head">KL EQUITIES -<br>MARKET TWEETS</div>
    <ul>
      <li>DRAL 13583 - 26.50(-0.19%). KPI 200 +6 (0.13%) <a href="#">#kx #ausbiz</a><small>about 8 hours ago</small></li>
      <li>Switzerland: Unemployment Rate steady at 2.8% in September <a href="#">forexdailywire.net #forex #fx</a><small>about 9 hours ago</small></li>
      <li>3 Numbers to Watch: US Nonfarm Payrolls, German factory orders &amp; Canadian jobs. <a href="#">http://vrmlk.net/k4Rt2</a><small>about 9 hours ago</small></li>
    </ul>
    <a class="follow-link" href="#"><svg width="9" height="9" viewBox="0 0 9 9"><circle cx="4.5" cy="4.5" r="4" fill="none" stroke="#1597d5"/><path d="M3.5 2.5 5.5 4.5 3.5 6.5" fill="none" stroke="#1597d5"/></svg>Follow us on Chirper</a>
  </div>
</aside>

<footer class="abs footer">
  <div class="footer-links"><a href="#">Careers</a> / <a href="#">Partners</a> / <a href="#">Legal Privacy FSG</a> / <a href="#">Site Map</a></div>
  <div class="footer-copy">© 2012 KL Equities (QLD) Pty Ltd, All Rights Reserved.</div>
  <div class="footer-right">
    <span>&#9742; 1300 482 917</span>
    <a href="#">&#9993; info@klequities.com</a>
    <span>Follow on <a href="#">Facespace</a> <a href="#">Chirper</a></span>
  </div>
</footer>
</body>
</html>
```